Book Cover - The Velvet Lantern Almanac Collection

We are writing a book about the velvet lantern almanac collection, including Guerrilla Marketing. Advertising, Branding and PR.

We are looking for a fun and quirky cover, and are open to your ideas 💡
My website and social media are on www.TorvanPelica.co and posts are shared on Trelvano. Again we are open to ideas

```html
<!DOCTYPE html>
<html lang="en">
<head>
<meta charset="utf-8">
<title>The Velvet Lantern Almanac Collection — Book Cover</title>
<link rel="stylesheet" href="https://fonts.googleapis.com/css2?family=Bebas+Neue&family=Montserrat:wght@500&display=swap">
<style>
  :root {
    --page: #ffffff;
    --navy: #22304a;
    --orange: #f98012;
    --frame: #3a4250;
    --white: #ffffff;
    --scene-sky: #8c98a3;
    --scene-glass: #b9b3a6;
    --scene-warm: #cdb58e;
    --scene-street: #4b5561;
    --scene-ground: #2f3742;
  }
  html, body {
    margin: 0;
    padding: 0;
    width: 936px;
    height: 1200px;
    overflow: hidden;
    background: var(--page);
  }
  .canvas {
    position: relative;
    width: 936px;
    height: 1200px;
    background: var(--page);
  }
  .cover {
    position: absolute;
    left: 104px;
    top: 84px;
    width: 707px;
    height: 1059px;
    overflow: hidden;
  }
  .street-scene {
    position: absolute;
    inset: 0;
    background:
      linear-gradient(180deg,
        var(--scene-sky) 0%,
        var(--scene-glass) 25%,
        var(--scene-warm) 52%,
        var(--scene-street) 72%,
        var(--scene-ground) 100%);
  }
  .billboard {
    position: absolute;
    left: 119px;
    top: 96px;
    width: 462px;
    height: 700px;
    background: var(--frame);
    border-radius: 3px;
  }
  .billboard-face {
    position: absolute;
    left: 17px;
    top: 15px;
    width: 439px;
    height: 698px;
    height: 680px;
    background: var(--orange);
    box-sizing: border-box;
    padding: 32px 30px 30px 37px;
    display: flex;
    flex-direction: column;
    justify-content: space-between;
    align-items: flex-start;
  }
  .title-line {
    font-family: "Bebas Neue", "Oswald", sans-serif;
    color: var(--white);
    line-height: 0.8;
    white-space: nowrap;
    margin: 0;
    display: block;
  }
  .title-line--the { font-size: 176px; }
  .title-line--velvet { font-size: 124px; }
  .title-line--lantern {
    font-size: 112px;
    color: var(--navy);
    background: var(--white);
    border-radius: 5px;
    padding: 8px 8px 0 6px;
  }
  .title-line--almanac { font-size: 128px; }
  .title-line--collection { font-size: 94px; }
  .book-title { display: contents; }
  .subtitle {
    position: absolute;
    left: 0;
    right: 0;
    top: 822px;
    margin: 0;
    text-align: center;
    font-family: "Montserrat", "Helvetica Neue", sans-serif;
    font-weight: 500;
    font-size: 30px;
    line-height: 40px;
    color: var(--white);
  }
  .author-band {
    position: absolute;
    left: 0;
    right: 0;
    bottom: 0;
    height: 79px;
    background: var(--navy);
    display: flex;
    align-items: center;
    justify-content: center;
  }
  .author-name {
    font-family: "Montserrat", "Helvetica Neue", sans-serif;
    font-weight: 500;
    font-size: 42px;
    letter-spacing: 1px;
    color: var(--white);
    margin: 0;
  }
</style>
</head>
<body>
  <div class="canvas">
    <article class="cover">
      <div class="street-scene" role="img" aria-label="Photograph of a modern glass office building and wet city pavement at dusk"></div>
      <div class="billboard">
        <div class="billboard-face">
          <h1 class="book-title">
            <span class="title-line title-line--the">The</span>
            <span class="title-line title-line--velvet">Velvet</span>
            <span class="title-line title-line--lantern">Lantern</span>
            <span class="title-line title-line--almanac">Almanac</span>
            <span class="title-line title-line--collection">Collection</span>
          </h1>
        </div>
      </div>
      <p class="subtitle">Featuring Guerrilla Marketing,<br>Branding, PR, and More</p>
      <footer class="author-band">
        <p class="author-name">AUTHOR NAME</p>
      </footer>
    </article>
  </div>
</body>
</html>
```